Corporate speaking flyer for email

Redesign existing and very lame flyer. This is for my speaking business to be used as an introduction of content and style and my presentations. More photos can be provided. As you will see I'm an adventurer who makes part of my living from speaking about my adventures. The bio describes the general gist of that. There is more I could say but wanting to keep it pretty brief so as not to bore potential clients. Having said that I'd like to try and capture them in the first instance.

Target Market(s)

Corporate, clubs, events

Industry/Entity Type

Business

Requirements
Must have
• bio and references. Content provided. Feel free to edit.
Nice to have
• Surprise me!
Should not have
• Rude words.

```html
<!DOCTYPE html>
<html lang="en">
<head>
<meta charset="utf-8">
<title>Ned Carrow – Speaker Flyer</title>
<link href="https://fonts.googleapis.com/css2?family=Oswald:wght@500&family=Lobster&family=Arimo:wght@400;700&display=swap" rel="stylesheet">
<style>
:root{
  --navy:#1f2f66;
  --navy-light:#3e5597;
  --tan:#b48c58;
  --tan-light:#cfae7f;
  --paper:#f1f2f4;
  --sea:#e3e6ea;
  --ink:#222;
  --bg:#c8c8c8;
  --white:#fff;
}
*{box-sizing:border-box;margin:0;padding:0}
html,body{width:1200px;height:1200px;overflow:hidden;background:var(--bg)}
body{position:relative;font-family:Arimo,Arial,sans-serif;color:var(--ink)}
.page{position:absolute;width:556px;height:760px;background:linear-gradient(180deg,var(--paper),var(--sea) 60%,var(--paper));overflow:hidden}
.page--bio{left:28px;top:54px}
.page--clients{left:613px;top:330px}

.stripe{position:absolute;left:0;right:0}
.tan-band{position:absolute;left:0;right:0;background:linear-gradient(90deg,var(--tan),var(--tan-light) 50%,var(--tan))}
.photo{position:absolute;border:3px solid var(--white)}

.bio-top{top:0;height:40px;background:linear-gradient(90deg,var(--navy),var(--navy-light))}
.bio-line{top:46px;left:180px;height:4px;background:var(--navy)}
.bio-line2{top:53px;left:180px;height:1.5px;background:var(--navy)}
.bio-photo{left:24px;top:19px;width:158px;height:172px;background:linear-gradient(135deg,#8a7a6a,#4a4038 60%,#2a2420)}
.bio-title{position:absolute;left:190px;width:316px;top:58px;text-align:center;font-family:Oswald,sans-serif;font-weight:500;color:var(--navy);font-size:33px;line-height:40px;letter-spacing:-.3px}
.bio-band{top:131px;height:59px}
.bio-quote{position:absolute;left:186px;top:136px;width:370px;font-family:Lobster,cursive;color:var(--white);font-size:18px;line-height:20px;padding-left:18px}
.qmark{color:var(--navy);font-family:Georgia,serif;font-weight:bold}
.bio-quote .qmark{font-size:24px;position:absolute;left:0;top:-2px}
.bio-text{position:absolute;left:24px;top:200px;width:506px;height:290px;padding:8px 6px;background:rgba(255,255,255,.45);font-size:8.2px;line-height:10.4px;text-align:justify}
.bio-text p{margin-bottom:6px}
.gallery{position:absolute;left:24px;top:498px;width:506px;height:205px;border:2px solid var(--navy);display:flex;gap:2px;background:var(--white)}
.gallery div{height:100%}
.gallery .ocean{width:236px;background:linear-gradient(160deg,#1c4a8a,#3a74b4 55%,#e8eef4 80%)}
.gallery .stage{flex:1;background:linear-gradient(180deg,#9a9a9a,#5c5c5c 55%,#cfcfcf)}

.footer{position:absolute;left:0;right:0;height:31px;background:linear-gradient(90deg,var(--tan),var(--tan-light) 50%,var(--tan));display:flex;align-items:center;justify-content:center;gap:12px;font-size:11px;color:var(--ink)}
.footer span{display:flex;align-items:center;gap:4px}
.footer svg{width:11px;height:11px}
.bio-footer{top:715px}
.clients-footer{top:711px}
.bottom-stripes{position:absolute;left:0;right:0;bottom:0;height:14px;background:linear-gradient(180deg,var(--navy) 0 5px,var(--white) 5px 7px,var(--navy) 7px 100%)}

.cl-top{top:0;height:9px;background:var(--navy)}
.cl-line{top:15px;height:4px;left:0;background:var(--navy)}
.cl-band{top:30px;height:35px}
.cl-photo{left:27px;top:12px;width:112px;height:76px;background:linear-gradient(135deg,#7a6250,#b38a6a 50%,#4a3a30)}
.cl-heading{position:absolute;left:168px;top:30px;width:360px;height:35px;line-height:35px;font-family:Lobster,cursive;color:var(--white);font-size:27px;letter-spacing:.5px}
.testimonials{position:absolute;left:20px;top:100px;width:510px;list-style:none}
.testimonials li{border-bottom:1px solid #c9ccd2;padding:0 0 4px;margin-bottom:5px}
.testimonials blockquote{position:relative;padding-left:6px;font-size:7.5px;line-height:10.3px;text-align:justify}
.testimonials .qmark{font-size:10px;line-height:0}
.testimonials .open{position:absolute;left:-2px;top:5px}
.testimonials cite{display:block;font-style:normal;font-weight:700;font-size:7.8px;margin:6px 0 0 6px}
</style>
</head>
<body>

<section class="page page--bio">
  <div class="stripe bio-top"></div>
  <div class="stripe bio-line"></div>
  <div class="stripe bio-line2"></div>
  <div class="tan-band bio-band"></div>
  <div class="photo bio-photo" role="img" aria-label="Portrait of the speaker gesturing while talking"></div>
  <h1 class="bio-title">NED CARROW<br>ANYTHING IS POSSIBLE</h1>
  <p class="bio-quote"><span class="qmark">“</span>An extraordinary mental and physical effort<br>- something very, very special <span class="qmark">”</span></p>

  <div class="bio-text">
    <p>Whether it’s laugh out loud humour, inspiration or thought provoking anecdotes and perspective, Ned Carrow’s deeply moving presentations has it all.</p>
    <p>“An extraordinary mental and physical effort – something very, very special” is how Sir Owen Fairlie described Ned Carrow and the late Sam Tully’s incredible achievement in winning the inaugural Transatlantic Row.</p>
    <p>Marathon rowing champion Ned Carrow has been a New Zealand International rowing representative for 16 years. Ned’s numerous rowing achievements include World Champs silver, Commonwealth gold and a world record on the indoor rowing machine.</p>
    <p>Ned represented New Zealand at the Atlanta Olympics and published ‘The Open Oar’ on how he and Sam Tully captured headlines around the world winning the grueling and inaugural Transatlantic Row in 41 days. He then led teams to successful defenses in the next two editions making it a 3-peat of victories for New Zealand.</p>
    <p>He is co-organiser of the ‘River 100’ (www.river100.example), ‘The Long Pull’ (www.thelongpull.example), an annual rowing 8s clash between Waikato and visiting international universities on the Waikato River. His also recently conceived and managed a rowing expedition across the Tasman Sea.</p>
    <p>Ambitious goal-setting, teamwork and overcoming adversity in multiple Transatlantic Row campaigns is the spine of Ned’s presentations, sandwiching the challenge of following his brother Liam’s journey into Cambodia’s Khmer Rouge genocide www.secondbrother.example (optional topic). Powerful inspiring messages on tenacity, hope, love and the last human freedom: the power to choose your attitude and how you respond in a given situation. The humour, the insights and the emotional turning points have audiences spellbound.</p>
    <p>Ned will inspire you to pursue your dreams whatever they may be, to take on new challenges, overcoming hardship against the odds and know that with passion anything is possible!</p>
    <p>&nbsp;It doesn’t hurt to be just a little bit crazy too!</p>
    <p>Ned’s life is about following the dream, decision making, commitment, team building, goal setting, planning, focus, determination, positive thinking and, of course, winning!</p>
  </div>

  <div class="gallery">
    <div class="ocean" role="img" aria-label="Two rowers celebrating with raised fists on their ocean rowing boat"></div>
    <div class="stage" role="img" aria-label="The speaker presenting on stage to a seated audience"></div>
  </div>

  <footer class="footer bio-footer">
    <span><svg viewBox="0 0 12 12"><rect x="1" y="2" width="10" height="6" fill="none" stroke="#222"/><path d="M4 10h4M6 8v2" stroke="#222"/></svg>www.nedcarrow.example</span>
    <span><svg viewBox="0 0 12 12"><rect x="1" y="3" width="10" height="7" fill="none" stroke="#222"/><path d="M1 3l5 4 5-4" fill="none" stroke="#222"/></svg>ned@tidemail.example</span>
    <span><svg viewBox="0 0 12 12"><path d="M1 5c0-2 10-2 10 0v1H8V5H4v1H1z M3 7h6l1 4H2z" fill="#222"/></svg>+64 (0)7 555 0142</span>
    <span><svg viewBox="0 0 12 12"><path d="M1 5c0-2 10-2 10 0v1H8V5H4v1H1z M3 7h6l1 4H2z" fill="#222"/></svg>+64 (0)21 555 01987</span>
  </footer>
  <div class="bottom-stripes"></div>
</section>

<section class="page page--clients">
  <div class="stripe cl-top"></div>
  <div class="stripe cl-line"></div>
  <div class="tan-band cl-band"></div>
  <div class="photo cl-photo" role="img" aria-label="Smiling portrait of the speaker"></div>
  <h2 class="cl-heading">What clients are saying .....</h2>

  <ul class="testimonials">
    <li><blockquote><span class="qmark open">“</span>Ned has a remarkable story, told in a clever and compelling way. He is able to engage deeply with his audience; he made us laugh, cry and most importantly think deeply, as leaders, about our role in the world. One of the best <span class="qmark">”</span></blockquote><cite>Clare Dunmore, HR Manager, Greenfield Dairy</cite></li>
    <li><blockquote><span class="qmark open">“</span>Young Hearts Trust was looking for an inspirational speaker who would reflect the passion, the hope and the commitment exhibited by YHT and its members. When I set out to look for such a person Ned Carrow’s name kept bubbling to the surface and I’m delighted I made the phone call. Ned your speech is probably the most inspiring talk I have ever listened to. Your story is an amazing one delivered in a passionate and yet entertaining manner. <span class="qmark">”</span></blockquote><cite>Tom Reddick, CEO Southern Plains Airport</cite></li>
    <li><blockquote><span class="qmark open">“</span>... hearing your story was more inspirational than all the traditional "motivational" type trainers put together. <span class="qmark">”</span></blockquote><cite>Mark Hollis, Hollis Property</cite></li>
    <li><blockquote><span class="qmark open">“</span>Ned was unbelievable, amazing, so well received, such a lovely guy, so humble. Had some of the audience in tears. <span class="qmark">”</span></blockquote><cite>Greg Lawton, Anchor Brokers Country Head</cite></li>
    <li><blockquote><span class="qmark open">“</span>The speaker was one of the most powerful I have listened to in years......incredible! <span class="qmark">”</span></blockquote><cite>From client taken from conference feedback form</cite></li>
    <li><blockquote><span class="qmark open">“</span>It was both an honour and a pleasure to be your host. The whole audience was captivated by your speech from start to finish. The clever way it was put together and how you incorporated our theme was fantastic. Your speech was truly inspirational and I personally have taken a lot out of it. The perspective on how I view challenges will change going forward as I am sure many others will too. I read a quote the other day that said 'Don't wait for sleep to dream' and I think that sums it up nicely. <span class="qmark">”</span></blockquote><cite>Sandra Kelby, Valley Regional Council</cite></li>
    <li><blockquote><span class="qmark open">“</span>One regular conference goer said I could organise another 50 conferences and not see a presentation as good as that. <span class="qmark">”</span></blockquote><cite>Lewis Farrant, Petrolink</cite></li>
    <li><blockquote><span class="qmark open">“</span>We have received nothing but the highest praise for your open and honest talk - many people have been deeply moved by your story and it was the highlight of the sessions. <span class="qmark">”</span></blockquote><cite>Hannah Pryor, Anchor Brokers EA to Country Head</cite></li>
    <li><blockquote><span class="qmark open">“</span>Listening to Ned speak is a breath of fresh air! Too often we come across heroes that seem untouchable, unattainable. But Ned's earthy humour and humble nature coupled with an unwavering drive and determination gives his story palpable appeal and something that the everyday person can truly connect with. Communicating with a passion that is infectious, Ned's story is one of triumph and tragedy and provides any listener the inspiration to get beyond the mindset of 'just getting by' when enduring tough or challenging times. He imparts the wisdom and notion that self- belief is critical and more importantly 'possible' for every one of us to achieve on our own personal journey to success. <span class="qmark">”</span></blockquote><cite>Julia Stavros, Campus Management, Melbourne</cite></li>
    <li><blockquote><span class="qmark open">“</span>Ned was outstanding. As requested he arrived early and set himself up with minimal assistance using our equipment. He was seated at the top table with some of our senior ranked officers and clearly struck a rapport early on, he skillfully (craftily) knitted some of this into the early part of his talk which was captivating and all were taken along on the roller coaster journey he portrays. He managed to lift the room initially before plummeting down into a deep and (not depressing) emotional low. This is done in such a way that he brings you along with him before raising your spirits once more and filling the room with laughter at the talks close. <span class="qmark">”</span></blockquote><cite>Capt Richard Bowden, Defence Training Unit</cite></li>
    <li><blockquote><span class="qmark open">“</span>I thought that you would be outstanding concluding Conference but I could not have expected the performance that you delivered. It blew everyone away Ned and it got in touch with their humanity which is what I wanted Physical Educators to go back to and to discover the power within. Thanks so very much for providing a conclusion to Conference that was extraordinarily powerful with such an invaluable message for all present. <span class="qmark">”</span></blockquote><cite>Graham Petrie, Physical Educators Guild</cite></li>
  </ul>

  <footer class="footer clients-footer">
    <span><svg viewBox="0 0 12 12"><rect x="1" y="2" width="10" height="6" fill="none" stroke="#222"/><path d="M4 10h4M6 8v2" stroke="#222"/></svg>www.nedcarrow.example</span>
    <span><svg viewBox="0 0 12 12"><rect x="1" y="3" width="10" height="7" fill="none" stroke="#222"/><path d="M1 3l5 4 5-4" fill="none" stroke="#222"/></svg>ned@tidemail.example</span>
    <span><svg viewBox="0 0 12 12"><path d="M1 5c0-2 10-2 10 0v1H8V5H4v1H1z M3 7h6l1 4H2z" fill="#222"/></svg>+64 (0)7 555 0142</span>
    <span><svg viewBox="0 0 12 12"><path d="M1 5c0-2 10-2 10 0v1H8V5H4v1H1z M3 7h6l1 4H2z" fill="#222"/></svg>+64 (0)21 555 01987</span>
  </footer>
  <div class="bottom-stripes"></div>
</section>

</body>
</html>
```